Local business providing residential house cleaning services

We need a business card design that is "cute" or "cartoonish" while still maintaining a professional appeal. Tidy Nook Cleaners is the name. We would like to use a "pin up girl" or maid next to the name with a broom or vacuum cleaner. We want the look to have a 50's American look to it. We are not sure if we want the pin up girl in a maid outfit or with a broom or vacuum cleaner but we hope some of you will be able to take these ideas and be creative. If you have any questions at all please don't hesitate to message me so that we can get the best design possible. Thank you very much and I look forward to seeing some designs! Mira Delgado

Target Market(s)

Upper class Americans that are busy and have money and want to come home to a clean house.

Industry/Entity Type

Cleaning Service

Contact Information for Business Card

Pin up girl incorporated into the card is a must.

Font styles to use
Decorative
Script

Requirements
Must have
• Pin up girl
Nice to have
• A crown used on the Q possibly.

```html
<!DOCTYPE html>
<html lang="en">
<head>
<meta charset="utf-8">
<title>Tidy Nook Cleaners – Business Card</title>
<link rel="stylesheet" href="https://fonts.googleapis.com/css2?family=Lobster&family=Lobster+Two&display=swap">
<style>
  :root {
    --backdrop-top: #ffffff;
    --backdrop-tint: #cfe9d8;
    --card-outer: #8fd0a6;
    --card-panel: #4ebd8d;
    --scallop: #000000;
    --ink-dark: #111111;
    --ink-light: #ffffff;
    --figure-dark: #1d1d1d;
    --figure-light: #f4efe9;
  }
  html, body {
    margin: 0;
    padding: 0;
    width: 1200px;
    height: 1000px;
    overflow: hidden;
  }
  body {
    position: relative;
    background: linear-gradient(180deg, var(--backdrop-tint) 0%, var(--backdrop-top) 18%, var(--backdrop-top) 82%, var(--backdrop-tint) 100%);
  }
  .business-card {
    position: absolute;
    left: 98px;
    top: 222px;
    width: 1005px;
    height: 556px;
  }
  .card-frame {
    position: absolute;
    inset: 0;
  }
  .pinup-figure {
    position: absolute;
    left: 62px;
    top: 40px;
    width: 200px;
    height: 460px;
    border-radius: 90px 90px 30px 30px;
    background: linear-gradient(180deg, var(--figure-dark) 0%, var(--figure-light) 45%, var(--figure-dark) 75%, #e9c9ad 100%);
  }
  .brand-name {
    position: absolute;
    left: 290px;
    top: 70px;
    width: 640px;
    margin: 0;
    font-family: "Lobster", cursive;
    font-weight: 400;
    font-size: 112px;
    line-height: 118px;
    color: var(--ink-light);
    text-align: center;
  }
  .brand-name span { display: block; }
  .owner-name {
    position: absolute;
    left: 240px;
    top: 352px;
    width: 720px;
    margin: 0;
    font-family: "Lobster", cursive;
    font-weight: 400;
    font-size: 50px;
    color: var(--ink-dark);
    text-align: center;
  }
  .contact {
    position: absolute;
    top: 438px;
    margin: 0;
    font-family: "Lobster Two", cursive;
    font-size: 27px;
    line-height: 38px;
    color: var(--ink-dark);
    text-align: center;
  }
  .contact dt, .contact dd { margin: 0; }
  .contact-phone { left: 250px; width: 200px; }
  .contact-email { left: 555px; width: 340px; }
</style>
</head>
<body>
  <article class="business-card">
    <svg class="card-frame" width="1005" height="556" viewBox="0 0 1005 556" aria-hidden="true">
      <rect x="0" y="0" width="1005" height="556" fill="var(--card-outer)"/>
      <g fill="var(--scallop)">
        <rect x="40" y="16" width="925" height="524" rx="80"/>
        <circle cx="90" cy="22" r="24"/><circle cx="140" cy="22" r="24"/><circle cx="190" cy="22" r="24"/>
        <circle cx="240" cy="22" r="24"/><circle cx="290" cy="22" r="24"/><circle cx="340" cy="22" r="24"/>
        <circle cx="390" cy="22" r="24"/><circle cx="440" cy="22" r="24"/><circle cx="490" cy="22" r="24"/>
        <circle cx="540" cy="22" r="24"/><circle cx="590" cy="22" r="24"/><circle cx="640" cy="22" r="24"/>
        <circle cx="690" cy="22" r="24"/><circle cx="740" cy="22" r="24"/><circle cx="790" cy="22" r="24"/>
        <circle cx="840" cy="22" r="24"/><circle cx="890" cy="22" r="24"/><circle cx="930" cy="40" r="24"/>
        <circle cx="90" cy="534" r="24"/><circle cx="140" cy="534" r="24"/><circle cx="190" cy="534" r="24"/>
        <circle cx="240" cy="534" r="24"/><circle cx="290" cy="534" r="24"/><circle cx="340" cy="534" r="24"/>
        <circle cx="390" cy="534" r="24"/><circle cx="440" cy="534" r="24"/><circle cx="490" cy="534" r="24"/>
        <circle cx="540" cy="534" r="24"/><circle cx="590" cy="534" r="24"/><circle cx="640" cy="534" r="24"/>
        <circle cx="690" cy="534" r="24"/><circle cx="740" cy="534" r="24"/><circle cx="790" cy="534" r="24"/>
        <circle cx="840" cy="534" r="24"/><circle cx="890" cy="534" r="24"/><circle cx="930" cy="516" r="24"/>
        <circle cx="46" cy="90" r="24"/><circle cx="46" cy="140" r="24"/><circle cx="46" cy="190" r="24"/>
        <circle cx="46" cy="240" r="24"/><circle cx="46" cy="290" r="24"/><circle cx="46" cy="340" r="24"/>
        <circle cx="46" cy="390" r="24"/><circle cx="46" cy="440" r="24"/><circle cx="46" cy="490" r="24"/>
        <circle cx="960" cy="90" r="24"/><circle cx="960" cy="140" r="24"/><circle cx="960" cy="190" r="24"/>
        <circle cx="960" cy="240" r="24"/><circle cx="960" cy="290" r="24"/><circle cx="960" cy="340" r="24"/>
        <circle cx="960" cy="390" r="24"/><circle cx="960" cy="440" r="24"/><circle cx="960" cy="490" r="24"/>
      </g>
      <rect x="62" y="36" width="880" height="484" rx="72" fill="var(--card-panel)"/>
    </svg>

    <div class="pinup-figure" role="img" aria-label="Illustration of a 1950s pin-up maid in black dress and white apron holding a feather duster"></div>

    <h1 class="brand-name"><span>Tidy Nook</span><span>Cleaners</span></h1>

    <p class="owner-name">Mira Delgado</p>

    <dl class="contact contact-phone">
      <dt>Phone:</dt>
      <dd>501-555-0142</dd>
    </dl>
    <dl class="contact contact-email">
      <dt>Email:</dt>
      <dd>miradelgado25@example.com</dd>
    </dl>
  </article>
</body>
</html>
```